Party invitation with a difference

I have recently turned 65, and I am holding a party for a number of my friends

I am looking for a stylish party invitation possibly in the guise of a rock concert admission ticket./ poster

promoting my band Blue Kettle who will be playing.at the party. We are a middle of the road covers band

I am turning 65 years so something like 65 and still Rocking ...

The party will run from 7.00pm until 11.00pm

Food platter and drink supplied.

No presents please

Date Saturday 30 June 2018
At Marlow & Fenn Restaurant, 718, Pebble Lane. Clevedon, Auckland 2617

RSVP to dennis.halloway@wirefold.co.nz

Target Market(s)

I have a guest list

Font styles to use

Colors

Designer to choose colors to be used in the design.

Requirements
Must have
• I will want to email the invitation to my guests as well as be able to print some off .
Nice to have
• The invitation is from Dennis and Marjorie Halloway
Should not have
• Not be flowery

```html
<!DOCTYPE html>
<html lang="en">
<head>
<meta charset="utf-8">
<title>Blue Kettle – 65th Birthday Invitation</title>
<link rel="stylesheet" href="https://fonts.googleapis.com/css2?family=Montserrat:wght@800&family=Oswald:wght@600&family=Roboto+Condensed:wght@700&family=Yellowtail&display=swap">
<style>
  :root {
    --backdrop: #3a3a3a;
    --night: #050308;
    --cream: #f6e7bd;
    --headline-yellow: #f4e420;
    --white: #ffffff;
  }
  * { margin: 0; padding: 0; box-sizing: border-box; }
  html, body { width: 1200px; height: 1200px; overflow: hidden; }
  body { background: var(--backdrop); position: relative; }

  .invitation {
    position: absolute;
    left: 261px; top: 162px;
    width: 678px; height: 876px;
    overflow: hidden;
    background: var(--night);
  }
  .concert-scene {
    position: absolute; inset: 0;
    background:
      radial-gradient(ellipse 55% 32% at 50% 30%, rgba(255,235,120,.9), transparent 70%),
      radial-gradient(ellipse 40% 28% at 45% 22%, rgba(159,196,42,.55), transparent 70%),
      radial-gradient(ellipse 70% 42% at 88% 25%, rgba(233,118,31,.85), transparent 75%),
      radial-gradient(ellipse 60% 42% at 8% 30%, rgba(210,90,40,.85), transparent 75%),
      linear-gradient(180deg, #5a2a18 0%, #b7641e 28%, #6b3a1a 48%, var(--night) 62%);
  }
  .stage-bowl { position: absolute; inset: 0; }

  .line { position: absolute; left: 0; right: 0; text-align: center; white-space: nowrap; }

  .tagline {
    font-family: "Oswald", sans-serif; font-weight: 600;
    font-size: 28px; line-height: 32px; color: var(--cream);
  }
  .tagline-1 { top: 38px; }
  .tagline-2 { top: 72px; }

  .celebrate {
    top: 410px;
    font-family: "Yellowtail", cursive; font-size: 44px; line-height: 50px; color: var(--cream);
  }
  .birthday {
    top: 458px;
    font-family: "Roboto Condensed", sans-serif; font-weight: 700;
    font-size: 32px; line-height: 50px; color: var(--cream);
  }
  .birthday sup { font-size: 17px; }
  .birthday .script { font-family: "Yellowtail", cursive; font-size: 42px; font-weight: 400; }

  .band-name {
    top: 516px;
    font-family: "Montserrat", sans-serif; font-weight: 800;
    font-size: 80px; line-height: 92px; color: var(--white);
  }

  .detail { font-family: "Roboto Condensed", sans-serif; font-weight: 700; color: var(--headline-yellow); }
  .day { top: 622px; font-size: 24px; line-height: 28px; letter-spacing: 9px; padding-left: 9px; }
  .date { top: 650px; font-size: 46px; line-height: 50px; }
  .time { top: 702px; font-size: 18px; line-height: 22px; }
  .venue { font-size: 15.5px; line-height: 20px; }
  .venue-1 { top: 728px; }
  .venue-2 { top: 748px; }

  .rsvp { font-family: "Roboto Condensed", sans-serif; font-weight: 700; color: var(--white); }
  .rsvp-label { top: 774px; font-size: 20px; line-height: 22px; }
  .rsvp-email { top: 797px; font-size: 15.5px; line-height: 20px; }
</style>
</head>
<body>
  <main class="invitation">
    <div class="concert-scene" role="img" aria-label="Rock concert scene: band and cheering crowd in silhouette under golden and orange stage lights"></div>

    <svg class="stage-bowl" width="678" height="876" viewBox="0 0 678 876" aria-hidden="true">
      <defs>
        <radialGradient id="ring-glow" cx="0.5" cy="0.5" r="0.5">
          <stop offset="0.7" stop-color="#e8482c"/>
          <stop offset="0.86" stop-color="#f07a3a"/>
          <stop offset="1" stop-color="#d9508a" stop-opacity="0"/>
        </radialGradient>
        <linearGradient id="floor-glow" x1="0" y1="0" x2="0" y2="1">
          <stop offset="0" stop-color="#2a0c18" stop-opacity="0"/>
          <stop offset="1" stop-color="#c9558c"/>
        </linearGradient>
      </defs>
      <rect x="0" y="640" width="678" height="236" fill="url(#floor-glow)"/>
      <circle cx="339" cy="580" r="360" fill="url(#ring-glow)"/>
      <circle cx="339" cy="580" r="260" fill="#050308"/>
      <rect x="0" y="500" width="678" height="150" fill="#050308"/>
    </svg>

    <p class="line tagline tagline-1">PARTY LIKE</p>
    <p class="line tagline tagline-2">A ROCK STAR!</p>

    <p class="line celebrate">Join us to celebrate</p>
    <p class="line birthday">My 65<sup>th</sup> <span class="script">Birthday</span></p>

    <h1 class="line band-name">Blue Kettle</h1>

    <p class="line detail day">SATURDAY</p>
    <p class="line detail date">30 JUNE 2018</p>
    <p class="line detail time">7.00pm – 11.00pm</p>
    <p class="line detail venue venue-1">At Marlow &amp; Fenn Restaurant, 718, Pebble Lane.</p>
    <p class="line detail venue venue-2">Clevedon, Auckland 2617</p>
    <p class="line rsvp rsvp-label">RSVP</p>
    <p class="line rsvp rsvp-email">dennis.halloway@wirefold.co.nz</p>
  </main>
</body>
</html>
```